Core Values Poster for Healthcare company

Trying to Create a core values poster for my company. Healthcare Company - We have Neurosurgery, Pain Management, Physical Therapy, Occupational Therapy, Rehab, Imaging, and psychology so far and we are growing fast.

Core Values would Include - (Execution), (Loyalty), (Innovation), (Synergy), (Growth-Oriented), (Ethics & Integrity), (Love), and (Energy)

Please incorporate the Company Logo which is on the website and I have included it in my uploads. As long as the logo stays blue it does not need a gradient effect.

I like the posters made for this contest : https://pinlarkstudio.com.au/flyer-work/briefs/build-team-ideals-flyer-580316

This picture should be memorable so people know our Core Values

Target Market(s)

Staff in the company

Colors

Designer to choose colors to be used in the design.

Requirements
Must have
• Logo
Nice to have
• Pictures for each core value

```html
<!DOCTYPE html>
<html lang="en">
<head>
<meta charset="utf-8">
<title>Clearview Core Values</title>
<link rel="stylesheet" href="https://fonts.googleapis.com/css2?family=Cinzel:wght@400&family=Oswald:wght@500&display=swap">
<style>
  :root {
    --paper: #ffffff;
    --brand-ink: #2b3440;
    --band-blue: #1b8edb;
    --text-light: #ffffff;
    --execution-a: #a81c66; --execution-b: #8a0a4c;
    --loyalty-a: #f9bb62; --loyalty-b: #f4a94c;
    --innovation-a: #0ea081; --innovation-b: #07906f;
    --synergy-a: #2bb4f0; --synergy-b: #1496de;
    --growth-a: #2447a8; --growth-b: #3558c8;
    --ethics-a: #8a2bd6; --ethics-b: #5e0ea8;
    --love-a: #e02232; --love-b: #f03444;
    --energy-a: #52a010; --energy-b: #3f9006;
  }
  * { box-sizing: border-box; margin: 0; padding: 0; }
  html, body { width: 726px; height: 1200px; overflow: hidden; background: var(--paper); }
  .poster { width: 726px; height: 1200px; padding: 0 22px; display: flex; flex-direction: column; }
  .brand {
    height: 100px; display: flex; align-items: center; justify-content: center;
    color: var(--brand-ink); font-family: "Oswald", sans-serif; font-weight: 500;
    font-size: 46px; letter-spacing: 3px;
  }
  .values-band {
    height: 48px; background: var(--band-blue); color: var(--text-light);
    font-family: "Cinzel", serif; font-size: 30px; letter-spacing: 9px;
    display: flex; align-items: center; justify-content: center;
  }
  .values-grid {
    flex: 1; margin: 10px 0 20px; display: grid;
    grid-template-columns: 1fr 1fr; grid-template-rows: repeat(4, 1fr); gap: 5px;
  }
  .value-tile {
    position: relative; display: flex; align-items: center; justify-content: center;
    color: var(--text-light); font-family: "Oswald", sans-serif; font-weight: 500;
    font-size: 34px; letter-spacing: 0.5px; overflow: hidden;
  }
  .value-icon {
    position: absolute; width: 150px; height: 170px; border-radius: 50%;
    background: rgba(0,0,0,0.12); top: 50%; left: 50%; transform: translate(-50%, -50%);
  }
  .value-name { position: relative; white-space: nowrap; }
  .execution { background: linear-gradient(135deg, var(--execution-a), var(--execution-b)); }
  .loyalty { background: linear-gradient(135deg, var(--loyalty-a), var(--loyalty-b)); }
  .loyalty .value-icon { background: rgba(230,140,40,0.35); }
  .innovation { background: linear-gradient(135deg, var(--innovation-a), var(--innovation-b)); }
  .synergy { background: linear-gradient(135deg, var(--synergy-a), var(--synergy-b)); }
  .growth { background: linear-gradient(135deg, var(--growth-a), var(--growth-b)); }
  .ethics { background: linear-gradient(135deg, var(--ethics-a), var(--ethics-b)); }
  .love { background: linear-gradient(135deg, var(--love-a), var(--love-b)); }
  .energy { background: linear-gradient(135deg, var(--energy-a), var(--energy-b)); }
</style>
</head>
<body>
<main class="poster">
  <header class="brand">
    <span class="brand-name">CLEARVIEW</span>
  </header>
  <div class="values-band">CORE VALUES</div>
  <section class="values-grid">
    <div class="value-tile execution"><div class="value-icon" role="img" aria-label="Icon of a person with a gear"></div><span class="value-name">EXECUTION</span></div>
    <div class="value-tile loyalty"><div class="value-icon" role="img" aria-label="Icon of a hand holding a heart"></div><span class="value-name">LOYALTY</span></div>
    <div class="value-tile innovation"><div class="value-icon" role="img" aria-label="Icon of a light bulb with gears"></div><span class="value-name">INNOVATION</span></div>
    <div class="value-tile synergy"><div class="value-icon" role="img" aria-label="Icon of an atom"></div><span class="value-name">SYNERGY</span></div>
    <div class="value-tile growth"><div class="value-icon" role="img" aria-label="Icon of rising bars with an arrow"></div><span class="value-name">GROWTH-ORIENTED</span></div>
    <div class="value-tile ethics"><div class="value-icon" role="img" aria-label="Icon of a figure holding balanced scales"></div><span class="value-name">ETHICS &amp; INTEGRITY</span></div>
    <div class="value-tile love"><div class="value-icon" role="img" aria-label="Icon of a heart"></div><span class="value-name">LOVE</span></div>
    <div class="value-tile energy"><div class="value-icon" role="img" aria-label="Icon of a lightning bolt in circular arrows"></div><span class="value-name">ENERGY</span></div>
  </section>
</main>
</body>
</html>
```